Law Firm Advertising Design Needed

Law Office of Dorvel K Tansy provides legal services to businesses and individuals who have been or are being injured. Our main practice area is personal injury (car accidents, wrongful death, premises liability), but we are looking for an ad that highlights a lesser known area of our practice - insurance company bad faith and breach of contract.

This ad will be placed in 8 1/2" x 11" format in a local neighborhood directory. It will also be placed in a smaller format (to be determined) in the local newspaper of a region of Arizona that has recently lost a considerable number of homes and people to wildfire.

We want to convey through the ad that our firm is available to help if their insurance company is not paying a legitimate claim or not paying enough for their claim.

Because of the tragic nature of the events in Yarnell, we would like to avoid images of fire or anything resembling fire. However, the ad should capture the attention of individuals who are struggling through an insurance claim with all the stacks of paperwork and frustrated with unresponsive adjusters and unreasonably low offers.

The design should convey a feeling of safety, security and being taken care of.

Information that must be included in the ad are: the firm name (Law Office of Dorvel K Tansy), address (4857 W 17th Avenue, Ste 406, Phoenix, AZ 85033), the phone number (602-574-2930) and the fact that we have mobile offices available to assist in your area.

An example of text that has been used in the past is here:
"If your own insurance company is refusing to pay what you are owed on a claim, call the Law Office of Dorvel K Tansy. We fight for you by examining the reasons your insurance carrier is denying or making an insufficient offer on the claim; updating and correcting claim documentation; making a new demand and filing a lawsuit if necessary. Whether it's a simple misunderstanding or something more complicated, we can help!

Here are a few of the kinds of claims we handle:
- Hit and Run or Uninsured driver claims
- Fire, flood and property loss
- Life insurance benefits
- Health insurance claims
- Catastrophic losses
- Business insurance
- Wrongful Death Benefits

Our attorneys are available to help you cut through the nonsense. Call to make an appointment for a free consultation with an attorney today. "

An example of a previous ad for car accident services is attached for reference.
Updates

Hi Everyone,

The main lawyer involved in the decision making process has been giving me some feedback in general on the designs that I thought I would pass along.  He does not want the name of the law firm to be the first thing you notice when you look at the ad. Try to keep that small and possibly to the bottom of the ad. The phone number should be rather large, but the address should be rather small (we are required by the State Bar to include our address, but we don't want our location to limit the location of our clients because our mobile offices can travel to them).  He would prefer that the logo either not be included or be not a significant part of the ad.

                                   

Thanks!  I will continue providing individual feedback to ads received. 

Target Market(s)

Low to middle income residents of the State of Arizona with little or no college education

Industry/Entity Type

Insurance

```html
<!DOCTYPE html>
<html lang="en">
<head>
<meta charset="utf-8">
<title>We Fight For You – Law Office of Dorvel K Tansy</title>
<link rel="stylesheet" href="https://fonts.googleapis.com/css2?family=Cinzel:wght@600;700&family=EB+Garamond:ital,wght@0,400;0,600;0,700;1,400;1,600&display=swap">
<style>
  :root {
    --bg: #ececec;
    --teal: #175470;
    --teal-light: #226a88;
    --teal-dark: #0f4058;
    --navy: #1b3d55;
    --navy-deep: #142c40;
    --white: #ffffff;
    --soft: #e6eef3;
    --tick: #8fd63a;
    --photo-warm: #c98a4e;
    --photo-cool: #6d7580;
  }
  * { box-sizing: border-box; margin: 0; padding: 0; }
  html, body { width: 1200px; height: 1000px; overflow: hidden; background: var(--bg); }
  .ad {
    position: absolute; left: 295px; top: 105px; width: 612px; height: 790px;
    background: var(--navy); color: var(--white);
    font-family: "EB Garamond", Georgia, serif;
    box-shadow: 0 4px 18px rgba(0,0,0,.25);
  }
  .band {
    position: absolute; left: 0; width: 100%;
    background: linear-gradient(180deg, var(--teal-light), var(--teal) 50%, var(--teal-dark));
    text-align: center;
  }
  .headline-band { top: 0; height: 75px; }
  .headline {
    font-family: "Cinzel", "Times New Roman", serif; font-weight: 700;
    font-size: 53px; line-height: 76px; letter-spacing: 1px;
  }
  .intro {
    position: absolute; left: 0; top: 75px; width: 100%; height: 257px;
    background: linear-gradient(180deg, var(--navy-deep), var(--navy) 60%, #22475f);
    padding: 12px 24px 0 24px;
  }
  .intro-text { font-size: 15.2px; line-height: 18.2px; text-align: justify; color: var(--soft); }
  .intro-text strong { color: var(--white); font-weight: 700; }
  .available { margin-top: 12px; font-style: italic; font-size: 15px; color: var(--soft); }
  .available strong { font-weight: 600; letter-spacing: .5px; }
  .claims { display: flex; margin-top: 8px; padding-left: 8px; }
  .claims ul { list-style: none; width: 330px; }
  .claims li { font-size: 15px; line-height: 18px; color: var(--soft); position: relative; padding-left: 18px; }
  .claims li.tick::before {
    content: "✓"; position: absolute; left: 0; top: 0; color: var(--tick); font-weight: 700;
  }
  .claims li.more { font-style: italic; }
  .cta-band { top: 332px; height: 80px; padding-top: 10px; }
  .cta-title { font-family: "Cinzel", "Times New Roman", serif; font-weight: 700; font-size: 31px; line-height: 36px; }
  .cta-sub { font-style: italic; font-size: 18px; line-height: 22px; }
  .cta-sub strong { font-style: normal; font-weight: 600; letter-spacing: .5px; }
  .photo {
    position: absolute; left: 0; top: 412px; width: 100%; height: 233px;
    background: linear-gradient(170deg, #3a3f46 0%, var(--photo-cool) 35%, var(--photo-warm) 60%, #e9d9a8 100%);
  }
  .firm-band { top: 645px; height: 46px; text-align: left; padding-left: 18px; }
  .firm-name { font-family: "Cinzel", "Times New Roman", serif; font-weight: 700; font-size: 21px; line-height: 46px; letter-spacing: .5px; }
  .footer {
    position: absolute; left: 0; top: 691px; width: 100%; height: 99px;
    background: linear-gradient(180deg, var(--navy), var(--navy-deep));
    padding: 14px 0 0 18px;
  }
  .address { font-size: 12px; color: var(--soft); }
  .phone { font-family: "Cinzel", "Times New Roman", serif; font-weight: 700; font-size: 27px; line-height: 36px; margin-top: 2px; }
  .phone span { margin-left: 12px; }
  .mobile { font-style: italic; font-size: 13px; color: var(--soft); }
  .website { position: absolute; right: 46px; bottom: 12px; font-family: Arial, sans-serif; font-size: 12px; }
  .brand {
    position: absolute; right: 30px; top: 610px;
    display: flex; align-items: center; gap: 10px;
  }
  .brand-mark { width: 22px; height: 22px; background: var(--white); }
  .brand-name { font-family: "EB Garamond", Georgia, serif; font-weight: 600; font-size: 30px; color: var(--white); }
</style>
</head>
<body>
  <main class="ad">
    <header class="band headline-band">
      <h1 class="headline">WE FIGHT FOR YOU</h1>
    </header>

    <section class="intro">
      <p class="intro-text">If your own insurance company is refusing to pay what you are owed on a claim, call the Law Office of Dorvel K Tansy. <strong>We fight for you</strong> by examining the reasons your insurance carrier is denying or making an insufficient offer on the claim; updating and correcting claim documentation; making a new demand and filing a lawsuit if necessary. Whether it's a simple misunderstanding or something more complicated, <strong>WE CAN HELP!</strong></p>
      <p class="available"><strong>OUR ATTORNEYS ARE AVAILABLE</strong> to help you cut through the nonsense.</p>
      <div class="claims">
        <ul>
          <li class="tick">Hit and Run or Uninsured driver claims</li>
          <li class="tick">Fire, flood and property loss</li>
          <li class="tick">Life insurance benefits</li>
          <li class="tick">Health insurance claims</li>
        </ul>
        <ul>
          <li class="tick">Catastrophic losses</li>
          <li class="tick">Business insurance</li>
          <li class="tick">Wrongful Death Benefits</li>
          <li class="more">and many more</li>
        </ul>
      </div>
    </section>

    <section class="band cta-band">
      <h2 class="cta-title">CALL TO MAKE AN APPOINTMENT</h2>
      <p class="cta-sub">for <strong>A FREE CONSULTATION</strong> with an attorney today!</p>
    </section>

    <div class="photo" role="img" aria-label="Photo: person at a desk holding a phone over a legal pad and an open planner"></div>

    <div class="brand">
      <span class="brand-mark"></span>
      <span class="brand-name">Tansy Law</span>
    </div>

    <section class="band firm-band">
      <p class="firm-name">LAW OFFICE OF DORVEL K. TANSY</p>
    </section>

    <footer class="footer">
      <p class="address">Law Office of Dorvel K. Tansy | 4857 W 17th Avenue, Ste 406, Phoenix, AZ 85033</p>
      <p class="phone">CALL US NOW!<span>602-574-2930</span></p>
      <p class="mobile">We have mobile offices available to assist in your area.</p>
      <p class="website">www.tansylaw.com</p>
    </footer>
  </main>
</body>
</html>
```